Residential home builder needs a fresh looking business card

We require a fresh looking business card for our business. We like the clean modern look. I have uploaded out logo and our email footer that incorporates some different elements. Blacks and Whites are good but i will leave this up to the design crowd creative minds.

our slogan is:
your idea of the perfect home

website (temporary site) but similar look and feel to the finished one
pinegrovedwellings.com.au

We also have intentions to apply the same look and feel to the rest of our stationary (letterheads, envelopes, site signs, vehicles etc)

Home Builder

```html
<!DOCTYPE html>
<html lang="en">
<head>
<meta charset="utf-8">
<title>PineGrove Dwellings – Business Card</title>
<link rel="stylesheet" href="https://fonts.googleapis.com/css2?family=Arimo:wght@400;700&display=swap">
<style>
  :root {
    --stage: #e9e6e2;
    --card-black: #262424;
    --card-white: #ffffff;
    --ink-dark: #1c1b1b;
    --gold: #f2c21b;
    --text-light: #f4f4f4;
    --font-body: "Arimo", Arial, sans-serif;
  }
  * { box-sizing: border-box; margin: 0; padding: 0; }
  html, body { width: 1200px; height: 800px; overflow: hidden; }
  body { background: var(--stage); font-family: var(--font-body); position: relative; }

  .card {
    position: absolute;
    width: 600px;
    height: 346px;
    background: var(--card-black);
    overflow: hidden;
    box-shadow: 0 6px 18px rgba(0,0,0,0.18);
  }

  /* Front: contact side */
  .card--front { left: 60px; top: 60px; }
  .card__header {
    height: 112px;
    background: var(--card-white);
    display: flex;
    align-items: center;
    justify-content: center;
  }
  .wordmark {
    font-family: var(--font-body);
    font-weight: 700;
    letter-spacing: 1px;
    white-space: nowrap;
  }
  .card__header .wordmark { color: var(--ink-dark); font-size: 38px; }

  .person { position: absolute; left: 0; width: 390px; top: 128px; text-align: center; }
  .person__name { color: var(--gold); font-weight: 700; font-size: 22px; }
  .person__role { color: var(--text-light); font-size: 16px; margin-top: 3px; }

  .contacts { position: absolute; left: 56px; top: 200px; list-style: none; }
  .contacts li {
    display: flex; align-items: center; gap: 12px;
    color: var(--text-light); font-size: 14.5px; letter-spacing: 0.3px;
    height: 22px;
  }
  .contacts li:nth-child(n+4) { height: 19px; }
  .contact-icon { width: 13px; height: 13px; flex: none; }

  /* Back: brand side */
  .card--back { left: 560px; top: 420px; }
  .brand-block {
    position: absolute; inset: 0;
    display: flex; flex-direction: column; align-items: center; justify-content: center;
    gap: 18px;
  }
  .brand-block__mark { width: 46px; height: 46px; background: var(--gold); }
  .card--back .wordmark { color: var(--text-light); font-size: 40px; }
  .brand-block__web { color: var(--gold); font-size: 15px; letter-spacing: 0.6px; margin-top: 22px; }
</style>
</head>
<body>

  <article class="card card--front">
    <header class="card__header">
      <span class="wordmark">PineGrove Dwellings</span>
    </header>

    <div class="person">
      <p class="person__name">Marcus Delany</p>
      <p class="person__role">General Manager</p>
    </div>

    <ul class="contacts">
      <li>
        <svg class="contact-icon" viewBox="0 0 13 13" aria-hidden="true"><rect width="13" height="13" rx="2" fill="#f2c21b"/><rect x="4" y="2" width="5" height="9" rx="1" fill="#262424"/><rect x="5" y="3" width="3" height="5" fill="#f2c21b"/></svg>
        <span>0400 555 218</span>
      </li>
      <li>
        <svg class="contact-icon" viewBox="0 0 13 13" aria-hidden="true"><rect width="13" height="13" rx="2" fill="#f2c21b"/><path d="M3 3.2c0 4 2.8 6.8 6.8 6.8l.8-1.8-2-1-1 1c-1.2-.5-2.3-1.6-2.8-2.8l1-1-1-2z" fill="#262424"/></svg>
        <span>08 5550 0142</span>
      </li>
      <li>
        <svg class="contact-icon" viewBox="0 0 13 13" aria-hidden="true"><rect width="13" height="13" rx="2" fill="#f2c21b"/><rect x="2.5" y="5" width="8" height="5" fill="#262424"/><rect x="4" y="2.5" width="5" height="3" fill="#262424"/></svg>
        <span>08 5550 0987</span>
      </li>
      <li>
        <svg class="contact-icon" viewBox="0 0 13 13" aria-hidden="true"><rect width="13" height="13" rx="2" fill="#f2c21b"/><rect x="2.5" y="3.5" width="8" height="6" fill="#262424"/><path d="M2.5 3.5l4 3.2 4-3.2" stroke="#f2c21b" fill="none"/></svg>
        <span>marcus@pinegrovedwellings.com.au</span>
      </li>
      <li>
        <svg class="contact-icon" viewBox="0 0 13 13" aria-hidden="true"><rect width="13" height="13" rx="2" fill="#f2c21b"/><circle cx="6.5" cy="6.5" r="4" fill="none" stroke="#262424" stroke-width="1.2"/><path d="M2.5 6.5h8M6.5 2.5c-2 2.5-2 5.5 0 8M6.5 2.5c2 2.5 2 5.5 0 8" stroke="#262424" fill="none" stroke-width="0.9"/></svg>
        <span>www.pinegrovedwellings.com.au</span>
      </li>
      <li>
        <svg class="contact-icon" viewBox="0 0 13 13" aria-hidden="true"><rect width="13" height="13" rx="2" fill="#f2c21b"/><path d="M6.5 11.2c-2-2.6-3-4.2-3-5.6a3 3 0 0 1 6 0c0 1.4-1 3-3 5.6z" fill="#262424"/><circle cx="6.5" cy="5.6" r="1.1" fill="#f2c21b"/></svg>
        <span>P.O Box 4410, Harlow Vale DC, WA 6999</span>
      </li>
    </ul>
  </article>

  <article class="card card--back">
    <div class="brand-block">
      <span class="brand-block__mark" aria-hidden="true"></span>
      <span class="wordmark">PineGrove Dwellings</span>
      <p class="brand-block__web">www.pinegrovedwellings.com.au</p>
    </div>
  </article>

</body>
</html>
```